Book cover The seven quiet ledgers

I need a book cover for a 6 x 9 inches book.

I prefer white background with clean lines. Bleed is 0.125 inches and spine is 0.27024

The back of the cover must consider the space for the ISBN barcode: 2" wide and 1.2" tall. The bottom of this ISBN barcode is located 1/4" up from the bottom trim line of the cover. The right side of the ISBN barcode is located 1/4" to the left of the spine.

Front cover should have title and subtitle plus author's name. The book is in Spanish so:

title: Las siete rutinas del desvelo
subtitle: Abra las puertas de su calma interior
author: Marta Quiroga Benning

the information about the book is here www.thesevenquietledgers.com

the back cover should have three blocks of information, a summary of the book, testimonials and about the author with a picture (leave space for a picture) Also, there should be a note with our website and bulk purchases

This is the information on the back. No need to add what is in parenthesis.

(about author) Marta Quiroga Benning es una de las expertas internacionales en creación de riqueza. Ha formado ocho empresas y una fundación, incluyendo el primer fondo de inversiones de capital semilla en Chile. Reconocida autora y expositora, ha recorrido el mundo varias veces presentando su sistema Brovanta®

Top (summary)
La mayoría de las personas no estan satisfechas con su prosperidad. Prueban estoy y aquello, hacen cursos, leen libros y mientras todos dicen lo que hay que hacer, nadie explica lo que NO hay que hacer. Si ud. Está estancado, este libro es para ud.

Testimonios (Testimonial):
Un libro que llega al alma. Tomás Verdún.
No solo es importante saber que hacer, sino estar alerta a lo que no debemos hacer. Derek Holloman.
El sistema para cambiar hábitos es excelente. Fernando Ubaldo-ruiz
Nos permite remendar esos pequeños detalles que afectan nuestra autoestima. Margaret Pruitt
Una manera sana de acumular y manejar la prosperidad que nos merecemos. Doreen Blick
Nos recuerda como nuestra percepción subconsciente del dinero afecta nuestro éxito financiero Renata Vail.

Ventas al mayor mpelorin@brovanta-mail.com
www.thesevenquietledgers.com

Target Market(s)

Individuals who feel they are working hard but are not getting the results they want regarding their financial well being.

this is NOT a book to get out of debt or to get rich quick.

this is a book for people who are serious about their lives and feel that, although they are working hard, they are stuck.

the summary of the book in English is found here: www.thesevenquietledgers.com
I am also changing working on the third edition of the book in English, so I wouldn't be using the same cover. you can see the book for sale on Librovia. "The Seven Quiet Ledgers"

Requirements
Must have
• Clean lines, white background, elegant, professional but human.
Nice to have
• an image that represents breaking a habit or getting unstuck. I thought about an anchor or a weigh or car brakes.
Should not have
• Bright colors, faces, pictures

```html
<!DOCTYPE html>
<html lang="es">
<head>
<meta charset="utf-8">
<title>Las siete rutinas del desvelo — cubierta</title>
<link rel="stylesheet" href="https://fonts.googleapis.com/css2?family=Oswald:wght@400;500&family=Roboto+Condensed:wght@400;700&family=Arimo&display=swap">
<style>
  :root {
    --stage: #000000;
    --paper: #ffffff;
    --ink: #111111;
    --band-dark: #000000;
    --band-grey: #9a9a9a;
    --band-gold: #b8925e;
    --photo-grey: #b3b3b3;
    --label: #ffffff;
    --accent: #b8925e;
  }
  * { margin: 0; padding: 0; box-sizing: border-box; }
  html, body { width: 1200px; height: 900px; overflow: hidden; background: var(--stage); }
  .stage { position: relative; width: 1200px; height: 900px; background: var(--stage); }

  .panel-label {
    position: absolute; top: 50px; color: var(--label);
    font-family: "Arimo", Arial, sans-serif; font-size: 24px; line-height: 30px;
    transform: translateX(-50%);
  }

  .panel { position: absolute; top: 92px; height: 685px; background: var(--paper); overflow: hidden; }
  .panel--back { left: 88px; width: 457px; }
  .panel--spine { left: 590px; width: 21px; }
  .panel--front { left: 655px; width: 457px; }

  .band { position: absolute; left: 0; right: 0; overflow: hidden; }
  .band--title { top: 90px; height: 58px; background: var(--band-dark); }
  .band--subtitle { top: 148px; height: 38px; background: var(--band-grey); }
  .band--author { top: 186px; height: 100px; background: var(--band-gold); }

  .band-text {
    position: absolute; white-space: nowrap; color: var(--paper);
    font-family: "Oswald", "Arial Narrow", sans-serif; text-transform: uppercase;
    font-stretch: condensed;
  }
  .band--title .band-text { font-weight: 500; font-size: 60px; line-height: 58px; top: -2px; letter-spacing: -1.5px; }
  .band--subtitle .band-text { font-weight: 400; font-size: 44px; line-height: 38px; top: 0; letter-spacing: -1.5px; }
  .band--author .band-text { font-weight: 500; font-size: 122px; line-height: 100px; top: 2px; letter-spacing: -3px; }

  .panel--front .band-text { left: 2px; }
  .panel--back .band--title .band-text { right: 183px; }
  .panel--back .band--subtitle .band-text { right: 297px; }
  .panel--back .band--author .band-text { right: 85px; }

  .isbn-space { position: absolute; left: 285px; top: 575px; width: 153px; height: 91px; background: var(--band-dark); }

  .spine-text {
    position: absolute; left: 50%; top: 608px; transform-origin: 0 0;
    transform: rotate(-90deg) translateY(-50%);
    white-space: nowrap; font-family: "Oswald", "Arial Narrow", sans-serif;
    font-weight: 500; font-size: 12px; line-height: 14px; text-transform: uppercase;
    color: var(--ink); letter-spacing: -0.3px;
  }
  .spine-text .spine-author { color: var(--accent); }

  .blurb {
    position: absolute; left: 28px; top: 312px; width: 300px;
    font-family: "Roboto Condensed", "Arial Narrow", sans-serif; font-size: 9.6px; line-height: 12.6px;
    color: var(--ink); text-align: justify;
  }
  .author-bio { display: flex; gap: 13px; }
  .author-photo { flex: 0 0 76px; height: 73px; background: var(--photo-grey); }
  .author-bio p { flex: 1; }
  .summary { margin-top: 16px; }
  .testimonials { margin-top: 16px; }
  .blurb strong { font-weight: 700; }
  .attribution { color: var(--accent); font-weight: 700; }

  .sales-note {
    position: absolute; left: 28px; top: 630px; width: 240px;
    font-family: "Roboto Condensed", "Arial Narrow", sans-serif; font-size: 9.6px; line-height: 12.6px;
    color: var(--ink);
  }
  .sales-note strong { font-weight: 700; }
  .sales-note .web { color: var(--accent); font-weight: 700; }
</style>
</head>
<body>
<div class="stage">
  <div class="panel-label" style="left:316px">Back</div>
  <div class="panel-label" style="left:600px">Spine</div>
  <div class="panel-label" style="left:884px">Front</div>

  <section class="panel panel--back" aria-label="Contraportada">
    <div class="band band--title"><span class="band-text">Las siete rutinas del desvelo</span></div>
    <div class="band band--subtitle"><span class="band-text">Abra las puertas de su calma interior</span></div>
    <div class="band band--author"><span class="band-text">Marta Quiroga Benning</span></div>

    <div class="blurb">
      <div class="author-bio">
        <div class="author-photo" role="img" aria-label="Espacio para la fotografía de la autora"></div>
        <p>Marta Quiroga Benning es una de las expertas internacionales en creación de riqueza. Ha formado ocho empresas y una fundación, incluyendo el primer fondo de inversiones de capital semilla en Chile. Reconocida autora y expositora, ha recorrido el mundo varias veces presentando su sistema Brovanta®</p>
      </div>
      <p class="summary"><strong>Top</strong> La mayoría de las personas no estan satisfechas con su prosperidad. Prueban estoy y aquello, hacen cursos, leen libros y mientras todos dicen lo que hay que hacer, nadie explica lo que NO hay que hacer. Si ud. Está estancado, este libro es para ud.</p>
      <p class="testimonials"><strong>Testimonios</strong> Un libro que llega al alma <span class="attribution">- Tomás Verdún</span> No solo es importante saber que hacer, sino estar alerta a lo que no debemos hacer <span class="attribution">- Derek Holloman</span> El sistema para cambiar hábitos es excelente <span class="attribution">- Fernando Ubaldo-ruiz</span> Nos permite remendar esos pequeños detalles que afectan nuestra autoestima <span class="attribution">- Margaret Pruitt</span> Una manera sana de acumular y manejar la prosperidad que nos merecemos <span class="attribution">- Doreen Blick</span> Nos recuerda como nuestra percepción subconsciente del dinero afecta nuestro éxito financiero <span class="attribution">- Renata Vail</span></p>
    </div>

    <p class="sales-note"><strong>Ventas al mayor</strong> mpelorin@brovanta-mail.com<br><span class="web">www.thesevenquietledgers.com</span></p>

    <div class="isbn-space" aria-label="Espacio reservado para el código ISBN"></div>
  </section>

  <section class="panel panel--spine" aria-label="Lomo">
    <div class="band band--title"></div>
    <div class="band band--subtitle"></div>
    <div class="band band--author"></div>
    <div class="spine-text">Las siete rutinas del desvelo <span class="spine-author">Marta Quiroga Benning</span></div>
  </section>

  <section class="panel panel--front" aria-label="Portada">
    <div class="band band--title"><h1 class="band-text">Las siete rutinas del desvelo</h1></div>
    <div class="band band--subtitle"><h2 class="band-text">Abra las puertas de su calma interior</h2></div>
    <div class="band band--author"><p class="band-text">Marta Quiroga Benning</p></div>
  </section>
</div>
</body>
</html>
```